Orva Business Card

we need a business card for flooring business called Orva Flooring, the design should be black and white. we have 2 locations

Marlowvale Showroom
527 Kellerman Road,
Marlowvale VIC 3147

Ashcombe Showroom
462 Bramwell Hwy,
Ashcombe VIC 3211

email : sales@orvaflooring.com.au
(03) 9471 2830

Please inform we sell , Laminate, Hybrid, Timber, carpet and commercial flooring

```html
<!DOCTYPE html>
<html lang="en">
<head>
<meta charset="utf-8">
<title>Orva Flooring – Business Card</title>
<link rel="stylesheet" href="https://fonts.googleapis.com/css2?family=Poppins:wght@400;600&display=swap">
<style>
  :root {
    --ink: #000000;
    --paper: #ffffff;
    --stripe: #3d3d3d;
    --backdrop: #e6e6e6;
    --card-w: 640px;
    --card-h: 391px;
  }
  * { box-sizing: border-box; margin: 0; padding: 0; }
  html, body { width: 1200px; height: 900px; overflow: hidden; }
  body {
    background: var(--backdrop);
    font-family: "Poppins", sans-serif;
    display: flex;
    flex-direction: column;
    align-items: center;
    justify-content: center;
    gap: 40px;
  }
  .card {
    position: relative;
    width: var(--card-w);
    height: var(--card-h);
    overflow: hidden;
    box-shadow: 0 6px 18px rgba(0,0,0,0.25);
  }

  /* Brand name */
  .brand {
    display: flex;
    align-items: center;
    gap: 14px;
  }
  .brand-dot {
    width: 22px;
    height: 22px;
    border-radius: 50%;
    flex: none;
  }
  .brand-name {
    font-weight: 400;
    font-size: 44px;
    letter-spacing: 3px;
    text-transform: uppercase;
    line-height: 1;
    white-space: nowrap;
  }

  /* Front */
  .card-front { background: var(--ink); color: var(--paper); }
  .card-front .brand {
    position: absolute;
    left: 0; right: 0;
    top: 140px;
    justify-content: center;
  }
  .card-front .brand-dot { background: var(--paper); }
  .services {
    position: absolute;
    left: 0; right: 0;
    bottom: 56px;
    text-align: center;
    font-size: 15px;
    font-weight: 400;
    letter-spacing: 0.3px;
  }

  /* Back */
  .card-back { background: var(--paper); color: var(--ink); }
  .card-back .brand {
    position: absolute;
    left: 34px;
    top: 176px;
    gap: 12px;
  }
  .card-back .brand-name { font-size: 29px; letter-spacing: 2px; }
  .card-back .brand-dot { background: var(--ink); width: 16px; height: 16px; }
  .contact {
    position: absolute;
    left: 378px;
    top: 28px;
    font-size: 13.5px;
    line-height: 1.28;
  }
  .showroom { margin-bottom: 7px; }
  .showroom-title { font-weight: 600; }
  .contact-line {
    display: flex;
    align-items: center;
    gap: 8px;
    margin-top: 3px;
  }
  .contact-line svg { width: 14px; height: 14px; flex: none; }
  .wave {
    position: absolute;
    left: 0; top: 0;
    width: 100%;
    height: 100%;
  }
  .website {
    position: absolute;
    right: 40px;
    bottom: 104px;
    color: var(--paper);
    font-size: 15px;
  }
</style>
</head>
<body>

  <section class="card card-front" aria-label="Card front">
    <div class="brand">
      <span class="brand-dot"></span>
      <span class="brand-name">Orva Flooring</span>
    </div>
    <p class="services">We Sell: Laminate, Hybrid, Timber, Carpet &amp; Commercial Flooring</p>
  </section>

  <section class="card card-back" aria-label="Card back">
    <svg class="wave" viewBox="0 0 640 391" preserveAspectRatio="none" aria-hidden="true">
      <path d="M0 322 C 150 314, 270 304, 390 270 C 480 242, 565 226, 640 224 L640 391 L0 391 Z" fill="var(--stripe)"/>
      <path d="M0 344 C 160 340, 280 324, 398 282 C 488 250, 568 232, 640 230 L640 391 L0 391 Z" fill="var(--ink)"/>
    </svg>

    <div class="brand">
      <span class="brand-dot"></span>
      <span class="brand-name">Orva Flooring</span>
    </div>

    <div class="contact">
      <div class="showroom">
        <div class="showroom-title">Marlowvale Showroom</div>
        <div>527 Kellerman Road,</div>
        <div>Marlowvale VIC 3147</div>
      </div>
      <div class="showroom">
        <div class="showroom-title">Ashcombe Showroom</div>
        <div>462 Bramwell Hwy,</div>
        <div>Ashcombe VIC 3211</div>
      </div>
      <div class="contact-line">
        <svg viewBox="0 0 24 24" aria-hidden="true"><path fill="currentColor" d="M6.6 10.8a15.1 15.1 0 0 0 6.6 6.6l2.2-2.2a1 1 0 0 1 1-.25 11.4 11.4 0 0 0 3.6.57 1 1 0 0 1 1 1V20a1 1 0 0 1-1 1A17 17 0 0 1 3 4a1 1 0 0 1 1-1h3.5a1 1 0 0 1 1 1c0 1.25.2 2.45.57 3.57a1 1 0 0 1-.25 1z"/></svg>
        <span>(03) 9471 2830</span>
      </div>
      <div class="contact-line">
        <svg viewBox="0 0 24 24" aria-hidden="true"><path fill="currentColor" d="M2 5h20v14H2z M4 7v.5l8 5 8-5V7l-8 5z" fill-rule="evenodd"/></svg>
        <span>sales@orvaflooring.com.au</span>
      </div>
    </div>

    <p class="website">orvaflooring.com.au</p>
  </section>

</body>
</html>
```